Visitenkarten-Design für modernes Industrieunternehmen
Zielgruppe
Wir stellen loses Füllmaterial (Schaumstoff-sticks, Latex-sticks und Visco-sticks) für Kopfkissen und Polstermöbel her. Auch Füllungen für Gartenauflagen sind in unserem Repertoire.
Aufgabenstellung
Wir liefern nicht an Endkunden, sondern nur an andere Unternehmen. Die Visitenkarte soll daher eine gewisse Seriösität ausstrahlen, aber trotzdem ins Auge fallen.

```html
<!DOCTYPE html>
<html lang="de">
<head>
<meta charset="utf-8">
<title>Flocora – Visitenkarte</title>
<link rel="stylesheet" href="https://fonts.googleapis.com/css2?family=Nunito+Sans:wght@400;800&display=swap">
<style>
  :root {
    --backdrop: #5b5b5b;
    --card: #f1f1f3;
    --brand-blue: #0f5fa0;
    --brand-teal: #1a8db6;
    --text-grey: #8c8c8c;
    --mark-grey: #8e8e8e;
    --icon-white: #ffffff;
  }
  * { margin: 0; padding: 0; box-sizing: border-box; }
  html, body {
    width: 1200px; height: 857px; overflow: hidden;
    background: var(--backdrop);
    font-family: "Nunito Sans", "Helvetica Neue", Arial, sans-serif;
  }
  .sheet {
    position: relative; width: 1200px; height: 857px;
    display: flex; justify-content: center; align-items: center; gap: 40px;
  }
  .card {
    position: relative; width: 520px; height: 336px;
    background: var(--card); overflow: hidden;
    box-shadow: 0 10px 28px rgba(0,0,0,0.35);
  }
  .card__shapes { position: absolute; inset: 0; width: 100%; height: 100%; }
  .contact-card__role {
    position: absolute; left: 56px; top: 108px;
    font-size: 31px; font-weight: 800; color: var(--brand-blue); letter-spacing: 0.5px;
  }
  .contact-card__name {
    position: absolute; left: 66px; top: 146px;
    font-size: 16px; font-weight: 400; color: var(--text-grey); letter-spacing: 0.4px;
  }
  .contact-list {
    position: absolute; left: 66px; top: 196px; list-style: none;
  }
  .contact-list__item {
    display: flex; align-items: center; gap: 12px; height: 24px;
    font-size: 16px; color: var(--text-grey); letter-spacing: 0.3px;
  }
  .contact-list__icon { width: 18px; height: 16px; flex: none; }
  .brand {
    position: absolute; left: 70px; top: 116px;
    display: flex; align-items: center; gap: 22px;
  }
  .brand__dot {
    width: 84px; height: 84px; border-radius: 50%; background: var(--mark-grey);
  }
  .brand__name {
    font-size: 66px; font-weight: 800; color: var(--brand-blue); letter-spacing: 1px; line-height: 1;
  }
</style>
</head>
<body>
<main class="sheet">

  <section class="card contact-card" aria-label="Vorderseite">
    <svg class="card__shapes" viewBox="0 0 520 336" aria-hidden="true">
      <defs>
        <linearGradient id="stripe-fill" x1="0" y1="0" x2="1" y2="1">
          <stop offset="0" stop-color="#0f5fa0"/>
          <stop offset="1" stop-color="#1a8db6"/>
        </linearGradient>
      </defs>
      <polygon points="285,0 350,0 520,246 520,341" fill="url(#stripe-fill)"/>
      <polygon points="375,0 430,0 520,130 520,210" fill="url(#stripe-fill)"/>
    </svg>
    <h1 class="contact-card__role">Geschäftsleiter</h1>
    <p class="contact-card__name">Jonas Beispielmann</p>
    <ul class="contact-list">
      <li class="contact-list__item">
        <svg class="contact-list__icon" viewBox="0 0 18 16" aria-hidden="true">
          <rect width="18" height="16" fill="var(--brand-blue)"/>
          <path d="M5 4 L7 4 L8 6.5 L7 7.5 Q8 9.5 10 10.5 L11 9.5 L13.5 10.5 L13.5 12 Q8 12.5 5 4 Z" fill="var(--icon-white)"/>
        </svg>
        0300 7284910
      </li>
      <li class="contact-list__item">
        <svg class="contact-list__icon" viewBox="0 0 18 16" aria-hidden="true">
          <rect width="18" height="16" fill="var(--brand-blue)"/>
          <rect x="4" y="4.5" width="10" height="7" fill="none" stroke="var(--icon-white)" stroke-width="1"/>
          <polyline points="4,4.5 9,8.5 14,4.5" fill="none" stroke="var(--icon-white)" stroke-width="1"/>
        </svg>
        flocora@postfach.de
      </li>
      <li class="contact-list__item">
        <svg class="contact-list__icon" viewBox="0 0 18 16" aria-hidden="true">
          <rect width="18" height="16" fill="var(--brand-blue)"/>
          <circle cx="9" cy="8" r="4.5" fill="none" stroke="var(--icon-white)" stroke-width="1"/>
          <ellipse cx="9" cy="8" rx="2" ry="4.5" fill="none" stroke="var(--icon-white)" stroke-width="0.8"/>
          <line x1="4.5" y1="8" x2="13.5" y2="8" stroke="var(--icon-white)" stroke-width="0.8"/>
        </svg>
        www.flocora.com
      </li>
    </ul>
  </section>

  <section class="card brand-card" aria-label="Rückseite">
    <svg class="card__shapes" viewBox="0 0 520 336" aria-hidden="true">
      <polygon points="0,226 0,336 150,336" fill="var(--brand-blue)"/>
    </svg>
    <div class="brand">
      <span class="brand__dot"></span>
      <span class="brand__name">Flocora</span>
    </div>
  </section>

</main>
</body>
</html>
```